New Webpage for High Class Expert Witness Services Company

We are looking for a minimalist design for a webpage that just has our logo and an entry form offer to connect with one of our Liaisons.
The entry form should just ask for Name, Email, Contact Info and Description of Project.

Company Name is: The Marlow Crest Advisory Services

Number of Pages Required

1 page

```html
<!DOCTYPE html>
<html lang="en">
<head>
<meta charset="utf-8">
<title>The Marlow Crest Advisory Services</title>
<link href="https://fonts.googleapis.com/css2?family=Inter:wght@400;500&family=Playfair+Display:wght@400;600;700&display=swap" rel="stylesheet">
<style>
:root{
  --bg:#0b0b0b;
  --ink:#ebe8e4;
  --muted:#4a4a4a;
  --glow:#2a4258;
  --glow-core:#3f5566;
  --line:#bdbdbd;
  --footer:#4b4b4b;
  --photo-a:#c9ccd0;
  --photo-b:#1d2634;
}
*{margin:0;padding:0;box-sizing:border-box}
html,body{width:752px;height:1200px;overflow:hidden;background:var(--bg)}
body{position:relative;font-family:"Inter",sans-serif;color:var(--ink)}
.serif{font-family:"Playfair Display",serif}
.hero-glow{position:absolute;left:36px;top:0;width:680px;height:420px;
  background:radial-gradient(ellipse at 50% 40%,var(--glow-core) 0%,var(--glow) 30%,#16222e 60%,rgba(11,11,11,0) 78%)}
.brand{position:absolute;left:42px;top:8px;width:167px;height:39px;display:flex;align-items:center;gap:6px;padding-left:6px;background:#141414}
.brand-mark{width:12px;height:12px;background:var(--ink)}
.brand-name{font-family:"Playfair Display",serif;font-size:11px;font-weight:400;color:var(--ink);letter-spacing:.3px}
.nav{position:absolute;top:22px;left:462px;font-size:9.4px;letter-spacing:.2px}
.nav a{position:absolute;color:var(--ink);text-decoration:none;white-space:nowrap}
.eyebrow{position:absolute;left:0;width:752px;top:97px;text-align:center;font-size:19px;font-weight:600}
.eyebrow-rule{position:absolute;top:107px;height:1.5px;width:57px;background:var(--ink)}
.headline{position:absolute;left:0;width:752px;top:136px;text-align:center;font-size:37px;font-weight:700;line-height:46px}
.cta{position:absolute;left:298px;top:240px;width:157px;height:38px;border:1px solid var(--ink);display:flex;align-items:center;justify-content:center;font-size:13.5px;font-weight:600}
.form{position:absolute;left:144px;top:465px;width:464px;height:210px;border:1.5px solid #fff}
.field{position:absolute;border:1px solid var(--line);font-size:9.4px;padding:0 5px;display:flex;align-items:center;color:#cfcfcf}
.field.area{align-items:flex-start;padding-top:7px}
.label{position:absolute;left:14px;top:14px;font-size:9.4px;color:#cfcfcf}
.submit{position:absolute;left:13px;top:165px;width:214px;height:26px;background:var(--ink);color:#111;font-size:9.4px;display:flex;align-items:center;justify-content:center}
.portrait{position:absolute;left:88px;top:727px;width:241px;height:196px;background:linear-gradient(90deg,var(--photo-a) 0%,#8f97a0 45%,var(--photo-b) 100%)}
.quote{position:absolute;left:386px;top:760px;font-size:34.5px;line-height:45px;font-weight:400}
.service{position:absolute;top:976px;height:135px}
.divider{position:absolute;top:976px;width:1px;height:135px;background:#555}
.service .num{position:absolute;left:3px;top:0;font-family:"Playfair Display",serif;font-size:23px;color:var(--muted)}
.service h3{position:absolute;left:3px;top:42px;font-family:"Playfair Display",serif;font-weight:400;font-size:20px;white-space:nowrap}
.service p{position:absolute;left:0;top:75px;width:200px;font-size:9.4px;line-height:15.2px;color:var(--muted)}
.footer{position:absolute;left:0;top:1173px;width:752px;height:27px;background:var(--footer);font-size:8.4px;display:flex;align-items:center;justify-content:center;gap:20px}
</style>
</head>
<body>
<div class="hero-glow"></div>
<div class="brand"><span class="brand-mark"></span><span class="brand-name">MARLOW CREST ADVISORY</span></div>
<nav class="nav">
  <a style="left:0">ABOUT</a><a style="left:58px">SERVICES</a><a style="left:127px">APPROACH</a><a style="left:203px">CONTACT</a>
</nav>
<div class="eyebrow-rule" style="left:243px"></div>
<div class="eyebrow-rule" style="left:452px"></div>
<div class="eyebrow serif">Defense Services</div>
<h1 class="headline serif">Discreet Protection.<br>Strategic Precision.</h1>
<div class="cta serif">Contact With A Liaison</div>

<form class="form">
  <div class="label">Name</div>
  <div class="field" style="left:13px;top:47px;width:214px;height:26px">Email</div>
  <div class="field" style="left:235px;top:47px;width:214px;height:26px">Phone</div>
  <div class="field area" style="left:13px;top:95px;width:436px;height:48px">Project Description</div>
  <div class="submit">Request Contact</div>
</form>

<div class="portrait" role="img" aria-label="Portrait photograph of a liaison"></div>
<p class="quote serif">Security is a craft,<br>practiced<br>Request quietly.</p>

<div class="service" style="left:45px"><span class="num">01</span><h3>Executive Protection</h3><p>Lorem ipsum dolor sit amet, consectetur adipiscing elit. Integer rutrum enim quis enim sollicitudin bibendum. Proin egestas ipsum augue, vel scelerisque</p></div>
<div class="divider" style="left:253px"></div>
<div class="service" style="left:277px"><span class="num">02</span><h3>Risk Intelligence</h3><p>Lorem ipsum dolor sit amet, consectetur adipiscing elit. Integer rutrum enim quis enim sollicitudin bibendum. Proin egestas ipsum augue, vel scelerisque</p></div>
<div class="divider" style="left:484px"></div>
<div class="service" style="left:508px"><span class="num">03</span><h3>Medical Integration</h3><p>Lorem ipsum dolor sit amet, consectetur adipiscing elit. Integer rutrum enim quis enim sollicitudin bibendum. Proin egestas ipsum augue, vel scelerisque</p></div>

<footer class="footer"><span>© The Marlow Crest Advisory Services</span><span>|&nbsp;&nbsp; Privacy | Contact</span></footer>
</body>
</html>
```